Interior decorating services

I would like to have a business card created for my interior decorating business.

Target Market(s)

any one wishing to have their space decorated

Industry/Entity Type

Business

Contact Information for Business Card

Lorna J. Whitcombe ; 417-582-6094; quibfennet42@mailvoro.net

Font styles to use
Serif

Colors

Designer to choose colors to be used in the design.

Requirements
Must have
• nice colors that flow well, and the name of my business: NookWay Designs
Nice to have
• round logo looking design in the corner

```html
<!DOCTYPE html>
<html lang="en">
<head>
<meta charset="utf-8">
<title>NookWay Designs – Business Card</title>
<link rel="stylesheet" href="https://fonts.googleapis.com/css2?family=Josefin+Sans:wght@300;400&display=swap">
<style>
  :root {
    --backdrop: #e7e2d8;
    --card-white: #f3f3f3;
    --text-grey: #8d8f91;
    --teal: #159db5;
    --teal-deep: #0f849a;
    --teal-shade: #12889e;
    --ink-light: #eaf8fb;
  }
  * { margin: 0; padding: 0; box-sizing: border-box; }
  html, body {
    width: 1200px;
    height: 800px;
    overflow: hidden;
    background: var(--backdrop);
    font-family: "Josefin Sans", sans-serif;
    font-weight: 300;
  }
  .canvas { position: relative; width: 1200px; height: 800px; }

  .card {
    position: absolute;
    width: 525px;
    height: 300px;
    border-radius: 3px;
    overflow: hidden;
    box-shadow: 0 6px 18px rgba(0, 0, 0, 0.18);
  }

  /* Front card */
  .card-front {
    left: 60px;
    top: 110px;
    background: var(--card-white);
    display: flex;
    align-items: center;
    justify-content: center;
    gap: 16px;
  }
  .brand-dot {
    width: 46px;
    height: 46px;
    border-radius: 50%;
    background: var(--teal);
    flex: none;
  }
  .brand-name {
    font-size: 38px;
    color: var(--text-grey);
    letter-spacing: 0.5px;
    white-space: nowrap;
  }

  /* Back card */
  .card-back {
    left: 615px;
    top: 390px;
    background: linear-gradient(160deg, var(--teal) 0%, var(--teal-shade) 100%);
    color: var(--ink-light);
  }
  .decor-circle {
    position: absolute;
    right: -30px;
    top: -50px;
    width: 220px;
    height: 220px;
    border-radius: 50%;
    background: var(--teal-deep);
    opacity: 0.75;
  }
  .back-brand {
    position: absolute;
    left: 36px;
    top: 120px;
    display: flex;
    align-items: center;
    gap: 12px;
  }
  .back-brand .brand-dot {
    width: 34px;
    height: 34px;
    background: var(--ink-light);
  }
  .back-brand .brand-name {
    font-size: 28px;
    color: var(--ink-light);
  }
  .person-name {
    position: absolute;
    left: 84px;
    top: 174px;
    font-size: 24px;
    letter-spacing: 0.5px;
  }
  .contact-list {
    position: absolute;
    left: 84px;
    top: 212px;
    list-style: none;
  }
  .contact-item {
    display: flex;
    align-items: center;
    gap: 9px;
    margin-bottom: 7px;
  }
  .contact-icon {
    width: 20px;
    height: 20px;
    flex: none;
  }
  .contact-phone { font-size: 22px; }
  .contact-email { font-size: 17px; }
</style>
</head>
<body>
<main class="canvas">

  <section class="card card-front" aria-label="Business card front">
    <span class="brand-dot" aria-hidden="true"></span>
    <span class="brand-name">NookWay Designs</span>
  </section>

  <section class="card card-back" aria-label="Business card back">
    <span class="decor-circle" aria-hidden="true"></span>

    <div class="back-brand">
      <span class="brand-dot" aria-hidden="true"></span>
      <span class="brand-name">NookWay Designs</span>
    </div>

    <p class="person-name">Lorna J. Whitcombe</p>

    <ul class="contact-list">
      <li class="contact-item">
        <svg class="contact-icon" viewBox="0 0 20 20" aria-hidden="true">
          <circle cx="10" cy="10" r="10" fill="#eaf8fb"/>
          <rect x="6.5" y="4.5" width="7" height="11" rx="1.2" fill="none" stroke="#159db5" stroke-width="1.4"/>
          <line x1="9" y1="13.3" x2="11" y2="13.3" stroke="#159db5" stroke-width="1.2"/>
        </svg>
        <span class="contact-phone">417-582-6094</span>
      </li>
      <li class="contact-item">
        <svg class="contact-icon" viewBox="0 0 20 20" aria-hidden="true">
          <circle cx="10" cy="10" r="10" fill="#eaf8fb"/>
          <rect x="5" y="6.5" width="10" height="7" fill="none" stroke="#159db5" stroke-width="1.3"/>
          <polyline points="5,6.5 10,10.5 15,6.5" fill="none" stroke="#159db5" stroke-width="1.3"/>
        </svg>
        <span class="contact-email">quibfennet42@mailvoro.net</span>
      </li>
    </ul>
  </section>

</main>
</body>
</html>
```